Speech Pathology card for parents of young children

I need a professional, yet fun card for my speech and language pathology services.
I'm trying to offer my speech therapy services to parents of young children. These parents will most likely be women. I want the card to have a fun feel to it and have a concept of speech and language in it (kind of like the cartoon I've attached below showing a boy/girl talking).

I'd want a white background on the card and to bring in some bright colors as well.

Please include the KROV logo in a smaller size on a free corner of the card.

Target Market(s)

parents of young children

Contact Information for Business Card

must have my information and I'd like it to have the KROV logo (small) somewhere in the corner)

Font styles to use
Serif
Sans Serif

Colors

Designer to choose colors to be used in the design.

Requirements
Must have
• The card title should read: Speech-Language Pathologist
• Rosalind Pettry
• MS CCC-SLP/TSSLD (this under the name)
• 415 906 2283
• rosiepettry@kelvormail.net
Nice to have
• i'm looking for a card with a white background and a fun icon that encompasses speaking... similar to the one I've attached.

```html
<!DOCTYPE html>
<html lang="en">
<head>
<meta charset="utf-8">
<title>Rosalind Pettry – Speech-Language Pathologist</title>
<link href="https://fonts.googleapis.com/css2?family=Kaushan+Script&family=Roboto:wght@400;500&display=swap" rel="stylesheet">
<style>
  :root {
    --backdrop: #e9e6e1;
    --card-white: #ffffff;
    --green: #8cc63f;
    --green-light: #b5df63;
    --orange: #f5a623;
    --orange-light: #fbc246;
    --pink: #e0157f;
    --ink: #1b1b1b;
    --on-green: #ffffff;
  }
  * { box-sizing: border-box; margin: 0; padding: 0; }
  html, body { width: 1200px; height: 1023px; overflow: hidden; }
  body {
    background: var(--backdrop);
    font-family: "Roboto", Arial, sans-serif;
    position: relative;
  }
  .card {
    position: absolute;
    left: 100px; top: 226px;
    width: 1000px; height: 570px;
    border-radius: 28px;
    background: var(--card-white);
    overflow: hidden;
    box-shadow: 0 14px 40px rgba(0,0,0,.18);
  }
  .card-waves { position: absolute; inset: 0; width: 1000px; height: 570px; }
  .speaker-illustration {
    position: absolute;
    left: 50px; top: 100px;
    width: 170px; height: 190px;
    border-radius: 12px;
    background: radial-gradient(circle at 50% 45%, #f3f0ea 0%, #e4efe0 55%, #ffffff 100%);
  }
  .card-title {
    position: absolute;
    left: 240px; top: 128px;
    color: var(--pink);
    font-size: 28px;
    font-weight: 500;
    white-space: nowrap;
  }
  .association {
    position: absolute;
    right: 48px; top: 28px;
    display: flex; align-items: center; gap: 12px;
  }
  .association-dot {
    width: 46px; height: 46px; border-radius: 50%;
    background: var(--ink);
  }
  .association-name {
    font-size: 20px; font-weight: 500; color: var(--ink);
    letter-spacing: 2px;
  }
  .contact {
    position: absolute;
    right: 48px; top: 300px;
    text-align: right;
    color: var(--on-green);
  }
  .contact-name {
    font-family: "Kaushan Script", cursive;
    font-size: 42px;
    font-weight: 400;
    line-height: 1.1;
    white-space: nowrap;
  }
  .contact-credentials {
    font-size: 22px;
    margin-top: 6px;
    letter-spacing: .5px;
  }
  .contact-rule {
    width: 46px; height: 2px; background: var(--on-green);
    margin: 16px 0 12px auto;
  }
  .contact-line {
    display: flex; justify-content: flex-end; align-items: center; gap: 14px;
    font-size: 22px; margin-top: 10px;
    white-space: nowrap;
  }
  .contact-icon { width: 20px; height: 20px; }
</style>
</head>
<body>
  <article class="card">
    <svg class="card-waves" viewBox="0 0 1000 570" aria-hidden="true">
      <defs>
        <linearGradient id="greenFill" x1="0" y1="0" x2="1" y2="1">
          <stop offset="0" stop-color="var(--green-light)"/>
          <stop offset="1" stop-color="var(--green)"/>
        </linearGradient>
      </defs>
      <path transform="translate(-12,-34)" d="M1000,140 C740,140 640,280 540,390 C440,500 300,515 0,520" fill="none" stroke="var(--orange-light)" stroke-width="12"/>
      <path transform="translate(-6,-17)" d="M1000,140 C740,140 640,280 540,390 C440,500 300,515 0,520" fill="none" stroke="var(--orange)" stroke-width="7"/>
      <path d="M1000,140 C740,140 640,280 540,390 C440,500 300,515 0,520 L0,570 L1000,570 Z" fill="url(#greenFill)"/>
    </svg>

    <div class="speaker-illustration" role="img" aria-label="Sketch of a child calling out through a megaphone"></div>
    <h1 class="card-title">Speech-Language Pathologist</h1>

    <div class="association">
      <span class="association-dot"></span>
      <span class="association-name">KROV</span>
    </div>

    <section class="contact">
      <h2 class="contact-name">Rosalind Pettry</h2>
      <p class="contact-credentials">MS CCC-SLP/TSSLD</p>
      <div class="contact-rule"></div>
      <p class="contact-line">415 906 2283
        <svg class="contact-icon" viewBox="0 0 24 24" aria-hidden="true"><path d="M6.6 10.8a15 15 0 0 0 6.6 6.6l2.2-2.2c.3-.3.7-.4 1-.2 1.1.4 2.3.6 3.6.6.6 0 1 .4 1 1V20c0 .6-.4 1-1 1A17 17 0 0 1 3 4c0-.6.4-1 1-1h3.5c.6 0 1 .4 1 1 0 1.3.2 2.5.6 3.6.1.3 0 .7-.2 1z" fill="#fff"/></svg>
      </p>
      <p class="contact-line">rosiepettry@kelvormail.net
        <svg class="contact-icon" viewBox="0 0 24 24" aria-hidden="true"><rect x="3" y="5" width="18" height="14" rx="2" fill="none" stroke="#fff" stroke-width="2"/><path d="M3 7l9 6 9-6" fill="none" stroke="#fff" stroke-width="2"/></svg>
      </p>
    </section>
  </article>
</body>
</html>
```